Walk Through the Fog Step out, step up and into your best performance

BRIEF FOR BOOK FRONT COVER

• It needs to be iconic
• It needs to be a ‘clean’ design
• Needs to be seen on a bookshelf in an airport from 50 feet away
• No stick like figures/cartoon style or cutesy design
• The book appeals to both male and female readers
• This is a cross over book and covers a couple of genres like Marcus Televan’s book The Engine of Routine or Odile Fenwick’s Leaping Boldly. So it is primarily about taking better care of yourself personally, professionally and will appeal to those in business.
• The idea that a personal enriching life feeds into an engaged performer on the job – they feed off each other leading to increased engagement, productivity and fulfillment
• The dance analogy means that you are not sitting on the sidelines of your life or business
• It is laced with inspiring real life case studies
• Positioning of the book: People facing adversity and still come through better than ever and better equipped to what comes next.
• Want a cover that would attract a Pinnacle 50 CEO to buy the book for his staff
• My name as the author should be across the bottom KESTA VOREHAM MBA MCC
Updates

Project Deadline Extended Reason: A big thank you for all the designers who submitted a cover design and I have been spoilt for choiceI need to finalize the copy on the book cover and hence the need for an extension of time.Thanks for your understanding.Kesta Added Sunday, September 18, 2016

Target Market(s)

Professionals in the age group 25 - 55

Industry/Entity Type

Airport

Contact Information for Business Card

basic information and a very clean look

Logo Text

probably book title more important that it can be seen clearly when the size is reduced to a small size e.g. if sponsoring an event

Number of Pages Required

5+ page

Font styles to use
Sans Serif

Colors
ec1f27
f37122
abd037

Requirements
Must have
• info already provided

```html
<!DOCTYPE html>
<html lang="en">
<head>
<meta charset="UTF-8">
<title>Walk Through the Fog – Book Cover</title>
<link rel="stylesheet" href="https://fonts.googleapis.com/css2?family=Italianno&family=Montserrat:wght@400;500&display=swap">
<style>
  :root {
    --page-bg: #ffffff;
    --cover-deep-red: #6e0d08;
    --cover-red: #a3190f;
    --cover-orange: #f37122;
    --cover-amber: #f5a02c;
    --cover-yellow: #d9d23a;
    --cover-green: #abd037;
    --cover-olive: #5d5a12;
    --text-light: #ffffff;
  }

  * { margin: 0; padding: 0; box-sizing: border-box; }

  html, body {
    width: 1200px;
    height: 1000px;
    overflow: hidden;
    background: var(--page-bg);
  }

  .canvas {
    position: relative;
    width: 1200px;
    height: 1000px;
    display: flex;
    align-items: center;
    justify-content: center;
  }

  .book-cover {
    position: relative;
    width: 580px;
    height: 880px;
    overflow: hidden;
    color: var(--text-light);
  }

  .cover-artwork {
    position: absolute;
    inset: 0;
    background:
      radial-gradient(ellipse 38% 30% at 55% 72%, rgba(217, 210, 58, 0.95), rgba(217, 210, 58, 0) 100%),
      radial-gradient(ellipse 30% 35% at 90% 70%, rgba(171, 208, 55, 0.85), rgba(171, 208, 55, 0) 100%),
      radial-gradient(ellipse 45% 30% at 62% 42%, rgba(245, 160, 44, 0.95), rgba(243, 113, 34, 0) 100%),
      radial-gradient(ellipse 70% 45% at 50% 48%, rgba(243, 113, 34, 0.9), rgba(243, 113, 34, 0) 100%),
      linear-gradient(180deg, var(--cover-deep-red) 0%, var(--cover-red) 30%, #b8301a 55%, var(--cover-olive) 90%, #3e3a0c 100%);
  }

  .cover-title-block {
    position: absolute;
    top: 200px;
    left: 70px;
    right: 24px;
  }

  .cover-title {
    font-family: "Italianno", cursive;
    font-weight: 400;
    font-size: 72px;
    line-height: 1;
    text-align: right;
    white-space: nowrap;
  }

  .cover-subtitle {
    margin-top: 4px;
    padding-left: 10px;
    font-family: "Montserrat", sans-serif;
    font-weight: 400;
    font-size: 11.5px;
    letter-spacing: 0.4px;
    text-transform: uppercase;
    white-space: nowrap;
  }

  .cover-author {
    position: absolute;
    left: 0;
    right: 40px;
    bottom: 52px;
    text-align: center;
    font-family: "Montserrat", sans-serif;
    font-weight: 500;
    font-size: 14px;
    letter-spacing: 1px;
    text-transform: uppercase;
  }
</style>
</head>
<body>
  <main class="canvas">
    <article class="book-cover">
      <div class="cover-artwork" role="img" aria-label="Painted scene of a couple dancing in the rain beneath red and orange autumn trees, glowing yellow-green light behind them"></div>

      <header class="cover-title-block">
        <h1 class="cover-title">Walk Through the Fog</h1>
        <p class="cover-subtitle">Move on, rise up and stride into your finest work</p>
      </header>

      <p class="cover-author">Kesta Voreham&nbsp; MBA MCC</p>
    </article>
  </main>
</body>
</html>
```